Business Card Design

I am a GP with interest in Dermatology and Aesthetic Medicin, performing Botulinum Toxin Type A and Dermal Fillers treatmets in Cosmetic Dermatology clinic.

I am looking for a white colour, good quality white paper card may be of some special texture with black calligraphic writing but easy to read and not to wiggly- professional- looking.

Really appreciate your help.

Milena

Contact Information for Business Card

Cosmetic Dermatology Clinic

Dr Milena Ravitskaya, MBBS, MRCGP, DPD

Tel: 07915 462 170
milena@medpractice-mail.co.uk

```html
<!DOCTYPE html>
<html lang="en">
<head>
<meta charset="utf-8">
<title>Business Card – Cosmetic Dermatology Clinic</title>
<link rel="stylesheet" href="https://fonts.googleapis.com/css2?family=Great+Vibes&display=swap">
<style>
  :root {
    --backdrop: #e6e6e8;
    --card-white: #ffffff;
    --ink: #111111;
    --pattern-tone-a: #f4f4f4;
    --pattern-tone-b: #e9e9e9;
    --card-shadow: rgba(0, 0, 0, 0.14);
  }
  * { margin: 0; padding: 0; box-sizing: border-box; }
  html, body {
    width: 1200px;
    height: 900px;
    overflow: hidden;
    background: var(--backdrop);
  }
  .canvas {
    width: 1200px;
    height: 900px;
    display: flex;
    align-items: center;
    justify-content: center;
    gap: 60px;
  }
  .card {
    position: relative;
    width: 530px;
    height: 303px;
    background: var(--card-white);
    box-shadow: 0 6px 18px var(--card-shadow);
    overflow: hidden;
    font-family: "Great Vibes", cursive;
    color: var(--ink);
  }
  .card__pattern {
    position: absolute;
    inset: 0;
    background: linear-gradient(90deg, var(--pattern-tone-a), var(--pattern-tone-b) 50%, var(--pattern-tone-a));
    opacity: 0.6;
  }
  .card__content {
    position: relative;
    height: 100%;
    display: flex;
    flex-direction: column;
    align-items: center;
    justify-content: center;
    text-align: center;
  }
  .front .clinic-name { font-size: 26px; letter-spacing: 0.5px; line-height: 1.2; }
  .front .doctor-name { font-size: 38px; line-height: 1.2; }
  .front .credentials { font-size: 28px; letter-spacing: 1px; line-height: 1.3; }
  .back .card__content { justify-content: flex-start; padding-top: 80px; }
  .back .phone { font-size: 30px; letter-spacing: 1px; line-height: 1.2; }
  .back .email { font-size: 30px; line-height: 1.2; }
</style>
</head>
<body>
  <main class="canvas">
    <section class="card front">
      <div class="card__pattern" role="img" aria-label="Vertical wavy dotted line pattern across the card"></div>
      <div class="card__content">
        <p class="clinic-name">Cosmetic Dermatology Clinic</p>
        <p class="doctor-name">Dr. Milena Ravitskaya</p>
        <p class="credentials">MBBS, MRCGP, DPD</p>
      </div>
    </section>
    <section class="card back">
      <div class="card__pattern" role="img" aria-label="Vertical wavy dotted line pattern across the card"></div>
      <div class="card__content">
        <p class="phone">Tel: 07915 462 170</p>
        <p class="email">milena@medpractice-mail.co.uk</p>
      </div>
    </section>
  </main>
</body>
</html>
```